"The Lantern Orchard Almanac" needs a Book Cover Design

I need a book cover design for my book titled "The Lantern Orchard Almanac". The cover style needs to be consistent with my website: http://lantern-oa.example. I have uploaded some samples of covers that I think are along the right path. I utilize mind-maps or bubble maps heavily as visual aids throughout the book so I want to drive home the point that I use mind-maps/links between topics, etc to be effective in my job as an effective project manager. I even uploaded a sample photo of me that might work on the cover (a log of self-help books seem to have photos of authors on the covers) but I am open.

The ultimate message of the book - How to manage yourself and manage others in order to be an effective project manager.

If you do all the things in the book and take all the advice you too can become an effective project manager. The delivery style of the content to the reader is conversational in nature - Like I am in the person's living room providing advice based on my 20 years of experience.

The book also provides many different real-world tools (mostly mind-map templates) and charts/graphs to help a project manager manage their projects. Also I provide other tips to the reader (productivity, people and email related)

```html
<!DOCTYPE html>
<html lang="en">
<head>
<meta charset="utf-8">
<title>The Lantern Orchard Almanac – Book Cover</title>
<link rel="stylesheet" href="https://fonts.googleapis.com/css2?family=Cinzel:wght@400;600;700&family=PT+Sans+Narrow&display=swap">
<style>
  :root {
    --navy-deep: #061226;
    --navy-mid: #0d2547;
    --navy-light: #1b4578;
    --orange: #f7a22a;
    --white: #ffffff;
    --black: #000000;
    --silver-hi: #ffffff;
    --silver-lo: #a9adb3;
    --shadow: rgba(0, 0, 0, 0.85);
    --photo-a: #0b2340;
    --photo-b: #3f6f9c;
    --photo-c: #9cc3e4;
  }
  html, body {
    margin: 0;
    padding: 0;
    width: 1200px;
    height: 900px;
    overflow: hidden;
    background: var(--navy-deep);
  }
  .cover-spread {
    position: relative;
    width: 1200px;
    height: 900px;
    overflow: hidden;
    background: radial-gradient(ellipse at 55% 20%, var(--navy-light) 0%, var(--navy-mid) 40%, var(--navy-deep) 100%);
  }
  /* Back cover */
  .back-cover {
    position: absolute;
    left: 0; top: 0;
    width: 545px; height: 773px;
    font-family: "PT Sans Narrow", "Arial Narrow", sans-serif;
    color: var(--white);
    text-align: center;
    font-size: 18.5px;
    line-height: 27px;
  }
  .back-blurb {
    position: absolute;
    left: 30px; width: 485px;
    top: 136px;
    margin: 0;
  }
  .profile-heading {
    position: absolute;
    left: 0; width: 545px;
    top: 502px;
    margin: 0;
    font-size: 19px;
    font-weight: normal;
  }
  .profile-text {
    position: absolute;
    left: 30px; width: 485px;
    top: 541px;
    margin: 0;
  }
  .barcode-slot {
    position: absolute;
    left: 228px; top: 828px;
    width: 110px; height: 54px;
    background: var(--white);
    color: var(--black);
    font-family: Arial, Helvetica, sans-serif;
    font-size: 21px;
    line-height: 25px;
    text-align: center;
    padding-top: 3px;
    box-sizing: border-box;
  }
  /* Spine */
  .spine-the {
    position: absolute;
    left: 545px; width: 90px;
    top: 55px;
    margin: 0;
    text-align: center;
    font-family: "Cinzel", "Times New Roman", serif;
    font-weight: 700;
    font-size: 30px;
    color: var(--white);
    text-shadow: 2px 2px 3px var(--shadow);
  }
  .spine-title {
    position: absolute;
    left: 590px; top: 118px;
    transform-origin: 0 0;
    transform: rotate(90deg) translateY(-50%);
    white-space: nowrap;
    margin: 0;
    font-family: "Cinzel", "Times New Roman", serif;
    font-weight: 700;
    font-size: 36px;
    letter-spacing: 1px;
    color: var(--white);
    text-shadow: 3px -3px 4px var(--shadow);
  }
  /* Front cover */
  .front-photo {
    position: absolute;
    left: 628px; top: 430px;
    width: 572px; height: 343px;
    background:
      radial-gradient(ellipse at 25% 30%, var(--photo-c) 0%, transparent 35%),
      linear-gradient(160deg, var(--photo-a) 0%, var(--photo-b) 55%, var(--photo-a) 100%);
    -webkit-mask-image: linear-gradient(to bottom, transparent 0%, #000 25%);
    mask-image: linear-gradient(to bottom, transparent 0%, #000 25%);
  }
  .front-title {
    position: absolute;
    left: 675px; width: 480px;
    top: 70px;
    margin: 0;
    text-align: center;
    font-family: "Cinzel", "Times New Roman", serif;
    font-weight: 600;
    color: var(--silver-lo);
  }
  .title-line {
    display: block;
    background: linear-gradient(to bottom, var(--silver-hi) 20%, var(--silver-lo) 95%);
    -webkit-background-clip: text;
    background-clip: text;
    color: transparent;
    filter: drop-shadow(4px 4px 3px var(--shadow));
  }
  .title-the { font-size: 50px; line-height: 64px; }
  .title-word { font-size: 88px; line-height: 100px; }
  .title-rule {
    display: block;
    height: 3px;
    background: var(--white);
    margin: 0;
  }
  /* Author band */
  .author-band {
    position: absolute;
    left: 0; top: 773px;
    width: 1200px; height: 127px;
    background: var(--orange);
  }
  .author-name {
    position: absolute;
    margin: 0;
    font-family: "Cinzel", "Times New Roman", serif;
    font-weight: 700;
    color: var(--white);
    text-align: center;
    text-shadow: 2px 2px 3px var(--shadow);
  }
  .author-name--front {
    left: 628px; width: 572px;
    top: 805px;
    font-size: 46px;
    line-height: 56px;
  }
  .author-name--spine {
    left: 545px; width: 90px;
    top: 824px;
    font-size: 13px;
    line-height: 14px;
  }
</style>
</head>
<body>
<main class="cover-spread">
  <section class="back-cover">
    <p class="back-blurb">need a book cover design for my book titled "The Lantern Orchard Almanac". The cover style needs to be consistent with my website: http://lantern-oa.example. I have uploaded some samples of covers that I think are along the right path. I utilize mind-maps or bubble maps heavily as visual aids throughout the book so I want to drive home the point that I use mind-maps/links between topics, etc to be effective in my job as an effective project manager. I even uploaded a sample photo of me that might work on the cover (a log of self-help books seem to have photos of authors on the covers) but I am open.</p>
    <h2 class="profile-heading">AUTHOR’S PROFILE</h2>
    <p class="profile-text">need a book cover design for my book titled "The Lantern Orchard Almanac". The cover style needs to be consistent with my website: http://lantern-oa.example. I have uploaded some samples of covers that I think are along the right path. I utilize mind-maps</p>
  </section>

  <p class="spine-the">THE</p>
  <p class="spine-title">Lantern Orchard Almanac</p>

  <div class="front-photo" role="img" aria-label="Photo of a businessman in a suit touching a glowing virtual screen of strategy icons and charts"></div>

  <h1 class="front-title">
    <span class="title-line title-the">THE</span>
    <span class="title-rule"></span>
    <span class="title-line title-word">Lantern</span>
    <span class="title-rule"></span>
    <span class="title-line title-word">Orchard</span>
    <span class="title-rule"></span>
    <span class="title-line title-word">Almanac</span>
  </h1>

  <div class="author-band"></div>
  <div class="barcode-slot">BAR<br>CODE</div>
  <p class="author-name author-name--spine">AUTHOR’S<br>NAME</p>
  <p class="author-name author-name--front">AUTHOR’S NAME</p>
</main>
</body>
</html>
```